Brightmorrow - a website to encourage people to spend time in nature

I have a squarespace site with some content on it but the squarespace template doesn't completely suit my needs, I keep fiddling with the template but actually I need some professional help to get it looking the way I want and with the right 'mood'.
The website is for "Brightmorrow" - it will be a blog where I write about the importance of nature for good health. I also want to use the website to market services such as outdoor coaching, retreats and walking workshops.
This has been in my head for a LONG time and I currently only use instagram for micro-blogs but it's time for me to get this moving. I've previously engaged other designers on branding for it but they just didn't get it quite the way that I wanted it and I wasn't completely happy with the results. It's been a process for me as to what I want but in the meantime I just didn't come back to the design aspect of it now. I'm looking for a designer who understands the purpose of the website, the ethos and can help me realise this into a design that's clean, clear and simple.

Please note that I have a domain (brightmorrow.example) and a lot of content drafted on squarespace already. I have published it with password protection - password is brightmorrow2020 - it still has some of the original template on it, but does have some content. Don't take it as anything to follow in particular, i am looking for fresh eyes and fresh ideas.
Updates

Need extra days to review

Target Market(s)

There are three main groups that I want to target - people who are suffering from stress and anxiety, people who treat them and parents who want to get their kids outside (thereby preventing stress and anxiety)

Contact Information for Business Card

Clara Dunmore
Brightmorrow
Telephone +44 7946 203857
brightmorrow@mailbox.example

Logo Text

Brightmorrow - if that. I have an idea that the logo should have a leaf on it somewhere, or maybe just be a leaf.

Coding

Coded - Design and coding required

Number of Pages Required

5+ page

Font styles to use
Serif
Sans Serif

Colors
add136
33b8a4
34a6d7
3377b5

Requirements
Must have
• Space for lots of images. The ability for me to edit the pages if I need to. Be user friendly. Look beautiful.
• For an idea of the images I use and the content I'm interested in writing about have a look at @brightmorrow on instagram.
• That pop up about cookies so I am complying with data laws.
Should not have
• Must not be too 'busy' I'd like to avoid too much movement.

```html
<!DOCTYPE html>
<html lang="en">
<head>
<meta charset="utf-8">
<title>Contact — Brightmorrow</title>
<link rel="stylesheet" href="https://fonts.googleapis.com/css2?family=Cormorant+Garamond:wght@400;500;600&family=Montserrat:wght@400;500;600&display=swap">
<style>
  :root {
    --sage: #74908a;
    --ink: #111111;
    --paper: #ffffff;
    --mist: #f5f5f5;
    --line: #e2e2e2;
    --muted: #7a7a7a;
    --forest-dark: #1a140d;
    --forest-mid: #3a2c1c;
    --forest-light: #6b6470;
  }
  * { box-sizing: border-box; margin: 0; padding: 0; }
  html, body { width: 945px; height: 1200px; overflow: hidden; background: var(--paper); }
  body { position: relative; font-family: "Montserrat", sans-serif; color: var(--ink); }
  .abs { position: absolute; }

  /* Header */
  .site-header { position: absolute; left: 0; top: 0; width: 945px; height: 55px; background: var(--paper); }
  .brand { position: absolute; left: 27px; top: 12px; display: flex; align-items: center; gap: 16px; }
  .brand-mark { width: 34px; height: 34px; border: 1.2px solid var(--sage); border-radius: 50%; }
  .brand-name { font-family: "Cormorant Garamond", serif; font-weight: 600; font-size: 27px; color: var(--sage); line-height: 1; }
  .main-nav a { position: absolute; top: 23px; font-size: 8.2px; font-weight: 600; letter-spacing: 2px; color: var(--ink); text-decoration: none; }
  .main-nav a.is-current { color: var(--sage); }

  /* Hero */
  .hero { position: absolute; left: 0; top: 55px; width: 945px; height: 213px;
    background: linear-gradient(90deg, var(--forest-dark) 0%, var(--forest-mid) 35%, #2a2016 55%, var(--forest-light) 72%, #2b2118 88%, var(--forest-dark) 100%); }
  .hero-title { position: absolute; left: 0; width: 945px; top: 64px; text-align: center; font-family: "Cormorant Garamond", serif; font-weight: 500; font-size: 40px; color: #fff; }
  .breadcrumb { position: absolute; left: 0; width: 945px; top: 133px; text-align: center; font-family: "Cormorant Garamond", serif; font-size: 13.5px; color: #fff; }
  .breadcrumb .sep { font-family: "Montserrat", sans-serif; font-size: 8px; font-weight: 600; margin: 0 5px; }

  /* Socials */
  .socials-section { position: absolute; left: 0; top: 268px; width: 945px; height: 284px; background: var(--mist); }
  .eyebrow { position: absolute; left: 0; width: 945px; text-align: center; font-size: 11px; font-weight: 500; letter-spacing: 3px; color: var(--sage); }
  .socials-heading { position: absolute; left: 0; width: 945px; top: 70px; text-align: center; font-family: "Cormorant Garamond", serif; font-weight: 500; font-size: 38px; line-height: 44px; color: var(--ink); }
  .social-links { position: absolute; top: 186px; left: 404px; display: flex; gap: 4px; }
  .social-links a { display: block; width: 43px; height: 43px; border-radius: 50%; background: var(--ink); }

  /* Form */
  .field { position: absolute; border: 1px solid var(--line); background: #fff; font-size: 10px; font-weight: 500; color: var(--muted); padding: 0 12px; letter-spacing: 0.3px; }
  .field-short { height: 36px; line-height: 34px; width: 218px; top: 717px; }
  .field-message { left: 248px; top: 765px; width: 449px; height: 136px; padding-top: 9px; }
  .consent { position: absolute; left: 248px; top: 914px; display: flex; align-items: center; gap: 7px; font-size: 9.6px; font-weight: 500; color: var(--muted); letter-spacing: 0.3px; }
  .consent .box { width: 7px; height: 7px; border: 1px solid var(--muted); border-radius: 1px; }
  .send { position: absolute; right: 248px; top: 943px; font-family: "Cormorant Garamond", serif; font-size: 14px; color: var(--sage); padding-bottom: 3px; border-bottom: 1.2px solid var(--sage); }

  /* Footer brand */
  .footer-brand { position: absolute; left: 0; width: 945px; top: 1029px; display: flex; justify-content: center; align-items: center; gap: 26px; }
  .footer-brand .brand-mark { width: 54px; height: 58px; border-width: 1.5px; }
  .footer-brand .brand-name { font-size: 40px; }

  .site-footer { position: absolute; left: 0; top: 1157px; width: 945px; height: 43px; background: var(--sage); color: #fff; }
  .copyright { position: absolute; left: 144px; top: 16px; font-size: 7.4px; font-weight: 500; letter-spacing: 0.3px; }
  .footer-nav a { position: absolute; top: 17px; font-size: 7.4px; font-weight: 500; color: #fff; text-decoration: none; }
</style>
</head>
<body>
  <header class="site-header">
    <div class="brand"><span class="brand-mark"></span><span class="brand-name">Brightmorrow</span></div>
    <nav class="main-nav">
      <a style="left:496px">HOME</a>
      <a style="left:567px">ABOUT</a>
      <a style="left:642px">WHAT WE DO</a>
      <a style="left:751px">BLOG</a>
      <a class="is-current" style="left:819px">CONTACT</a>
    </nav>
  </header>

  <section class="hero" role="img" aria-label="Photograph of a dim pine forest with tall trunks and low sunlight">
    <h1 class="hero-title">Contact</h1>
    <p class="breadcrumb">Home<span class="sep">✕</span>Contact</p>
  </section>

  <section class="socials-section">
    <p class="eyebrow" style="top:40px">CONTACT ME</p>
    <h2 class="socials-heading">If You Have Any Questions<br>Feel Free To Find Me In Socials</h2>
    <div class="social-links">
      <a aria-label="Photo sharing profile"></a>
      <a aria-label="Social network page"></a>
      <a aria-label="Image board profile"></a>
    </div>
  </section>

  <p class="eyebrow" style="top:634px">OR MAIL ME</p>

  <div class="field field-short" style="left:248px">Enter YourName</div>
  <div class="field field-short" style="left:479px">Enter YourEmail</div>
  <div class="field field-message">Enter Your Message</div>
  <label class="consent"><span class="box"></span>I agree that my submitted data is being collected and stored</label>
  <span class="send">Send Message</span>

  <div class="footer-brand"><span class="brand-mark"></span><span class="brand-name">Brightmorrow</span></div>

  <footer class="site-footer">
    <p class="copyright">Brightmorrow © 2020 &nbsp;&nbsp;|&nbsp;&nbsp; All rights reserved</p>
    <nav class="footer-nav">
      <a style="left:565px">HOME</a>
      <a style="left:614px">ABOUT</a>
      <a style="left:665px">SERVICES</a>
      <a style="left:727px">BLOG</a>
      <a style="left:772px">CONTACT</a>
    </nav>
  </footer>
</body>
</html>
```